INSURANCE
RAY HOLLOWAY INSURANCE
Project: INSURANCE
INSURANCE -
Creative Brief
Cutting-Edge
20837 MAPLECREST DR SUITE 210 DALLAS TX 75251
rhollowayinsurance@mailvexo.com
rateyourcover.com
I am open for any suggestions on the Design type... On the back of the card "YOU" should stand out OR should be a larger Font.
ARE YOU TIRED OF PAYING TOO MUCH FOR INSURANCE..?? OUR EXPERTISE IN SHOPPING MULTIPLE PROVIDERS WILL SAVE "YOU" MONEY...$$

```html
<!DOCTYPE html>
<html lang="en">
<head>
<meta charset="utf-8">
<title>Ray Holloway Insurance – Stationery</title>
<link rel="stylesheet" href="https://fonts.googleapis.com/css2?family=Roboto:wght@400;700&display=swap">
<style>
  :root {
    --brand-red: #d42a2a;
    --brand-navy: #2b3a8f;
    --paper: #ffffff;
    --page-bg: #ffffff;
    --frame: #e4e4e4;
    --divider: #b9b9b9;
    --flap-line: #c8c8c8;
    --shadow: rgba(0, 0, 0, 0.28);
  }
  * { box-sizing: border-box; margin: 0; padding: 0; }
  html, body { width: 1200px; height: 681px; overflow: hidden; background: var(--page-bg); }
  body { font-family: "Roboto", Arial, sans-serif; position: relative; }

  .presentation-frame {
    position: absolute; left: 20px; top: 18px; width: 1160px; height: 630px;
    border: 1px solid var(--frame);
  }
  .sheet {
    position: absolute; background: var(--paper);
    box-shadow: 6px 8px 14px var(--shadow);
  }
  .brand-name {
    position: absolute; display: flex; align-items: center; gap: 0.4em;
    color: var(--brand-red); font-weight: 700; letter-spacing: 0.03em;
    line-height: 1.15; white-space: nowrap;
  }
  .brand-name::before {
    content: ""; flex: none; width: 0.8em; height: 0.8em; background: var(--brand-red);
  }
  .brand-name .brand-lines { display: block; text-align: center; }
  .divider { position: absolute; width: 1px; background: var(--divider); }
  .contact {
    position: absolute; color: var(--brand-navy); font-style: normal;
    line-height: 1.45; white-space: nowrap;
  }

  /* Envelope front */
  .envelope-front { left: 65px; top: 77px; width: 468px; height: 228px; }
  .envelope-front .brand-name { left: 18px; top: 40px; font-size: 11px; }
  .envelope-front .divider { left: 146px; top: 34px; height: 44px; }
  .envelope-front .contact { left: 156px; top: 36px; font-size: 7px; }

  /* Envelope back */
  .envelope-back { left: 65px; top: 360px; width: 468px; height: 216px; }
  .envelope-back svg { position: absolute; left: 0; top: 0; }
  .envelope-back .brand-name { left: 50%; top: 36px; transform: translateX(-50%); font-size: 9px; }

  /* Letterhead */
  .letterhead { left: 619px; top: 48px; width: 341px; height: 576px; }
  .letterhead .brand-name { left: 18px; top: 48px; font-size: 10px; }
  .letterhead .divider { left: 150px; top: 38px; height: 78px; }
  .letterhead .contact { left: 158px; top: 40px; font-size: 6.5px; }

  /* Business card front */
  .card-front { left: 967px; top: 180px; width: 197px; height: 115px; }
  .card-front .brand-name { left: 10px; top: 42px; font-size: 6px; }
  .card-front .divider { left: 88px; top: 16px; height: 80px; }
  .card-front .card-holder {
    position: absolute; left: 95px; top: 18px; font-size: 8px; color: var(--brand-red);
  }
  .card-front .contact { left: 95px; top: 34px; font-size: 5px; }

  /* Business card back */
  .card-back { left: 967px; top: 319px; width: 197px; height: 118px; }
  .card-back .tagline {
    position: absolute; left: 0; right: 0; top: 42px; text-align: center;
    color: var(--brand-navy); font-size: 5.2px; line-height: 1.9;
  }
  .card-back .tagline .you { color: var(--brand-red); font-weight: 700; font-size: 8px; }
</style>
</head>
<body>
  <div class="presentation-frame"></div>

  <section class="sheet envelope-front" aria-label="Envelope front">
    <div class="brand-name"><span class="brand-lines">RAY HOLLOWAY<br>INSURANCE</span></div>
    <div class="divider"></div>
    <address class="contact">20837 Maplecrest Dr<br>Suite 210<br>Dallas, TX 75251</address>
  </section>

  <section class="sheet envelope-back" aria-label="Envelope back">
    <svg width="468" height="216" viewBox="0 0 468 216" aria-hidden="true">
      <path d="M4 4 L22 46 Q30 58 50 60 L418 60 Q438 58 446 46 L464 4" fill="none" stroke="var(--flap-line)" stroke-width="1"/>
    </svg>
    <div class="brand-name"><span class="brand-lines">RAY HOLLOWAY<br>INSURANCE</span></div>
  </section>

  <section class="sheet letterhead" aria-label="Letterhead">
    <div class="brand-name"><span class="brand-lines">RAY HOLLOWAY<br>INSURANCE</span></div>
    <div class="divider"></div>
    <address class="contact">20837 Maplecrest Dr<br>Suite 210<br>Dallas, TX 75251<br>Phone: 972-555-0148<br>Fax: 972-555-0162<br>rhollowayinsurance@mailvexo.com<br>rateyourcover.com</address>
  </section>

  <section class="sheet card-front" aria-label="Business card front">
    <div class="brand-name"><span class="brand-lines">RAY HOLLOWAY<br>INSURANCE</span></div>
    <div class="divider"></div>
    <div class="card-holder">Ray Holloway</div>
    <address class="contact">20837 Maplecrest Dr<br>Suite 210<br>Dallas, TX 75251<br>Phone: 972-555-0148<br>Fax: 972-555-0162<br>rhollowayinsurance@mailvexo.com<br>rateyourcover.com</address>
  </section>

  <section class="sheet card-back" aria-label="Business card back">
    <p class="tagline">
      Are you tired of paying too much for insurance..??<br>
      Our expertise in shopping multiple providers will save<br>
      <span class="you">"YOU"</span> money...$$
    </p>
  </section>
</body>
</html>
```